Redesign our current website with a more professional feel

We currently have a running website that generates some traffic and looks ok but now we want to revamp it with professional eye catching design.
We are open to proposals and open to any new ideas or suggestions but we have to see your previous work.
our current site is www.kelbrin-works.com.au

Thank you for your time and we look forward to seeing your proposals

Target Market(s)

Business owners, managers

Industry/Entity Type

Security

Number of Pages Required

5+ page

```html
<!DOCTYPE html>
<html lang="en">
<head>
<meta charset="utf-8">
<title>Kelbrin Works — Security Services</title>
<link rel="stylesheet" href="https://fonts.googleapis.com/css2?family=Raleway:wght@400;500&family=Open+Sans:wght@400&display=swap">
<style>
  :root {
    --header-bg: #141416;
    --nav-active: #6a8bcd;
    --divider: #a3a3a3;
    --footer-bg: #000000;
    --white: #ffffff;
    --logo-ink: #2a3f8f;
    --overlay-blue: rgba(52, 92, 168, 0.86);
    --label: #ffffff;
    --shade: rgba(10, 12, 16, 0.55);
  }
  * { box-sizing: border-box; margin: 0; padding: 0; }
  html, body { width: 1200px; height: 1085px; overflow: hidden; background: var(--header-bg); }
  body { position: relative; font-family: "Open Sans", sans-serif; color: var(--white); }

  .site-header { position: absolute; left: 0; top: 0; width: 1200px; height: 111px; background: var(--header-bg); }
  .brand { position: absolute; left: 47px; top: 0; width: 214px; height: 110px; background: var(--white);
    display: flex; align-items: center; justify-content: center; gap: 8px; }
  .brand-dot { width: 12px; height: 12px; border-radius: 50%; background: var(--logo-ink); }
  .brand-name { font-family: "Raleway", sans-serif; font-weight: 500; font-size: 22px; color: var(--logo-ink); letter-spacing: 0.5px; }

  .main-nav a { position: absolute; top: 0; height: 110px; padding-top: 11px; display: flex; align-items: center; justify-content: center; gap: 6px;
    color: var(--white); text-decoration: none; font-size: 11.5px; text-transform: uppercase; transform: translateX(-50%); white-space: nowrap; }
  .main-nav a.is-active { background: var(--nav-active); width: 145px; left: 443px; }
  .main-nav svg { width: 12px; height: 12px; fill: var(--white); }

  .divider-bg { position: absolute; left: 0; top: 111px; width: 1200px; height: 877px; background: var(--divider); }

  .tile { position: absolute; overflow: hidden; }
  .tile-media { position: absolute; inset: 0; }
  .tile-media::after { content: ""; position: absolute; inset: 0;
    background: linear-gradient(180deg, rgba(10,12,16,0.15) 0%, var(--shade) 100%); }
  .tile-label { position: absolute; left: 0; right: 0; text-align: center; font-family: "Raleway", sans-serif;
    font-weight: 500; font-size: 17.5px; color: var(--label); }

  .feature-overlay { position: absolute; inset: 0; background: var(--overlay-blue); text-align: center; padding-top: 68px; }
  .feature-title { font-family: "Raleway", sans-serif; font-weight: 500; font-size: 19px; letter-spacing: 1.5px; }
  .feature-text { width: 370px; margin: 16px auto 0; font-size: 12px; line-height: 17px; }
  .read-more { display: inline-block; margin-top: 20px; width: 108px; height: 33px; line-height: 33px; background: var(--white); color: #222; font-size: 12px; text-decoration: none; }

  .site-footer { position: absolute; left: 0; top: 988px; width: 1200px; height: 97px; background: var(--footer-bg); }
  .copyright { position: absolute; left: 0; width: 1212px; top: 47px; text-align: center; font-family: "Raleway", sans-serif; font-size: 11.5px; color: #e0e0e0; }
  .social { position: absolute; top: 35px; width: 29px; height: 29px; border: 1.5px solid var(--white);
    display: flex; align-items: center; justify-content: center; }
  .social-mark { width: 9px; height: 9px; border-radius: 50%; background: var(--white); }
</style>
</head>
<body>
  <header class="site-header">
    <div class="brand"><span class="brand-dot"></span><span class="brand-name">KELBRIN WORKS</span></div>
    <nav class="main-nav">
      <a href="#" class="is-active"><svg viewBox="0 0 12 12"><path d="M6 1 L11 6 H9.5 V11 H7 V8 H5 V11 H2.5 V6 H1 Z"/></svg>Home</a>
      <a href="#" style="left:609px"><svg viewBox="0 0 12 12"><circle cx="6" cy="3.5" r="2.6"/><path d="M1 12 C1 7.5 11 7.5 11 12 Z"/></svg>About Us</a>
      <a href="#" style="left:758px"><svg viewBox="0 0 12 12"><circle cx="6" cy="6" r="4"/><circle cx="6" cy="6" r="1.5" fill="#141416"/><path d="M5 0h2v2H5zM5 10h2v2H5zM0 5h2v2H0zM10 5h2v2h-2z"/></svg>Service</a>
      <a href="#" style="left:919px"><svg viewBox="0 0 12 12"><rect x="3.5" y="0.5" width="5" height="5"/><rect x="0.5" y="6.5" width="5" height="5"/><rect x="6.5" y="6.5" width="5" height="5"/></svg>Special Offers</a>
      <a href="#" style="left:1109px"><svg viewBox="0 0 12 12"><path d="M2 1 L4.5 1 L5.5 4 L4 5 C5 7 6 8 8 9 L9 7.5 L12 8.5 L12 11 C6 12 0 6 2 1 Z"/></svg>Contact Us</a>
    </nav>
  </header>

  <main>
    <div class="divider-bg"></div>

    <section class="tile" style="left:0;top:112px;width:602px;height:295px">
      <div class="tile-media" role="img" aria-label="Operator monitoring a wall of CCTV screens in a control room"
        style="background:radial-gradient(ellipse 45% 55% at 28% 35%,#5d6a72 0%,rgba(93,106,114,0) 100%),radial-gradient(ellipse 30% 40% at 85% 20%,#7a7d80 0%,rgba(122,125,128,0) 100%),radial-gradient(ellipse 30% 45% at 85% 75%,#1b1c20 0%,rgba(27,28,32,0) 100%),linear-gradient(135deg,#454b52,#33373c 60%,#26282c)"></div>
      <h2 class="tile-label" style="top:255px">CONTROL ROOM</h2>
    </section>
    <section class="tile" style="left:605px;top:112px;width:595px;height:295px">
      <div class="tile-media" role="img" aria-label="Business handshake with a client in an office"
        style="background:radial-gradient(ellipse 30% 45% at 10% 50%,#8d8a86 0%,rgba(141,138,134,0) 100%),radial-gradient(ellipse 25% 40% at 50% 30%,#7a6d66 0%,rgba(122,109,102,0) 100%),radial-gradient(ellipse 30% 35% at 60% 75%,#8c8078 0%,rgba(140,128,120,0) 100%),radial-gradient(ellipse 25% 60% at 92% 30%,#1e1f24 0%,rgba(30,31,36,0) 100%),linear-gradient(120deg,#5c5a58,#4a4a4e 55%,#3a3b40)"></div>
      <h2 class="tile-label" style="top:254px">STATIC GUARDING</h2>
    </section>

    <section class="tile" style="left:0;top:409px;width:367px;height:283px">
      <div class="tile-media" role="img" aria-label="Hand holding a smartphone showing a patrol app"
        style="background:radial-gradient(ellipse 30% 50% at 45% 30%,#2b3336 0%,rgba(43,51,54,0) 100%),radial-gradient(ellipse 40% 40% at 70% 75%,#8a7060 0%,rgba(138,112,96,0) 100%),radial-gradient(ellipse 25% 30% at 5% 20%,#6e6a3e 0%,rgba(110,106,62,0) 100%),linear-gradient(135deg,#5a5644,#4a4740 50%,#5a4a40)"></div>
      <h2 class="tile-label" style="top:246px">MOBILE PATROL &amp; RESPONSE</h2>
    </section>
    <section class="tile" style="left:369px;top:409px;width:461px;height:283px">
      <div class="tile-media" role="img" aria-label="Reception desk with staff greeting visitors"
        style="background:radial-gradient(ellipse 30% 40% at 30% 35%,#c9cfd8 0%,rgba(201,207,216,0) 100%),radial-gradient(ellipse 25% 40% at 78% 30%,#a58d80 0%,rgba(165,141,128,0) 100%),linear-gradient(135deg,#8a95a8,#6d7890)"></div>
      <div class="feature-overlay">
        <h2 class="feature-title">CONCIERGE / RECEPTION</h2>
        <p class="feature-text">Lorem ipsum dolor sit amet, consectetur adipiscing elit, sed do eiusmod tempor incididunt ut laboreLorem ipsum dolor sit amet, consectetur adipiscing elit, sed do eiusmod</p>
        <a href="#" class="read-more">Read More</a>
      </div>
    </section>
    <section class="tile" style="left:832px;top:409px;width:368px;height:283px">
      <div class="tile-media" role="img" aria-label="Ceiling-mounted dome security camera"
        style="background:radial-gradient(ellipse 30% 35% at 55% 45%,#1a1c1e 0%,rgba(26,28,30,0) 100%),radial-gradient(ellipse 50% 30% at 40% 5%,#1e2022 0%,rgba(30,32,34,0) 100%),radial-gradient(ellipse 35% 45% at 15% 75%,#4d5a52 0%,rgba(77,90,82,0) 100%),linear-gradient(135deg,#4a5052,#3e4446 50%,#45504a)"></div>
      <h2 class="tile-label" style="top:244px">CCTV &amp; ALARM INSTALLATIONS</h2>
    </section>

    <section class="tile" style="left:0;top:694px;width:605px;height:292px">
      <div class="tile-media" role="img" aria-label="Person reviewing printed reports at a desk"
        style="background:radial-gradient(ellipse 30% 45% at 30% 30%,#9a968e 0%,rgba(154,150,142,0) 100%),radial-gradient(ellipse 30% 40% at 25% 85%,#8e8a84 0%,rgba(142,138,132,0) 100%),radial-gradient(ellipse 30% 50% at 75% 45%,#7a6450 0%,rgba(122,100,80,0) 100%),linear-gradient(135deg,#554e45,#46403a 55%,#4e4438)"></div>
      <h2 class="tile-label" style="top:252px">LATEST NEWS</h2>
    </section>
    <section class="tile" style="left:608px;top:694px;width:592px;height:292px">
      <div class="tile-media" role="img" aria-label="Interlocking gears with one highlighted in red"
        style="background:radial-gradient(circle at 55% 42%,#8a2a30 0%,rgba(138,42,48,0.5) 12%,rgba(0,0,0,0) 28%),radial-gradient(ellipse 30% 40% at 70% 70%,#7a7a7e 0%,rgba(122,122,126,0) 100%),radial-gradient(ellipse 40% 45% at 30% 40%,#4a4c52 0%,rgba(74,76,82,0) 100%),linear-gradient(135deg,#34363b,#2c2e33 45%,#24262a)"></div>
      <h2 class="tile-label" style="top:246px">CUSTOMER FEEDBACK</h2>
    </section>
  </main>

  <footer class="site-footer">
    <p class="copyright">Copyright 2016 Company Name.&nbsp; All Rights Reserved.</p>
    <a href="#" class="social" style="left:1038px" aria-label="Social profile 1"><span class="social-mark"></span></a>
    <a href="#" class="social" style="left:1081px" aria-label="Social profile 2"><span class="social-mark"></span></a>
    <a href="#" class="social" style="left:1123px" aria-label="Social profile 3"><span class="social-mark"></span></a>
  </footer>
</body>
</html>
```